Ridgeway Framers Business Card

I'm looking for a business card design for a start-up Handyman/Construction Company. The organization will double as a ministry to the homeless, hoping to create job opportunity and training to the homeless, providing a pathway back to being "homed". I'm looking for a simple to "seeming" simple design. Open to all thoughts.

Industry/Entity Type

Ministry

Requirements
Must have
• Logo (Attached), Name, Phone, Email and Address. Note - "*Registered and Insured".

```html
<!DOCTYPE html>
<html lang="en">
<head>
<meta charset="utf-8">
<title>Ridgeway Framers Business Card</title>
<link href="https://fonts.googleapis.com/css2?family=Questrial&display=swap" rel="stylesheet">
<style>
  :root {
    --backdrop: #e8e7ed;
    --card-white: #fbfcfc;
    --navy: #22304f;
    --strip-grey: #cfd4d5;
    --base-grey: #eceeee;
    --band-text: #e9edf3;
    --divider: #5a6784;
  }
  * { margin: 0; padding: 0; box-sizing: border-box; }
  html, body {
    width: 1200px; height: 934px; overflow: hidden;
    background: var(--backdrop);
    font-family: "Questrial", sans-serif;
  }
  .business-card {
    position: absolute; left: 180px; top: 227px;
    width: 840px; height: 480px;
    background: var(--card-white);
    box-shadow: 0 10px 30px rgba(40, 40, 70, 0.12);
    overflow: hidden;
  }
  .brand {
    position: absolute; left: 72px; top: 138px;
    display: flex; align-items: center; gap: 18px;
  }
  .brand-mark {
    width: 56px; height: 56px; background: var(--navy); flex: none;
  }
  .brand-text { display: flex; flex-direction: column; align-items: flex-end; }
  .company-name {
    font-size: 50px; line-height: 1; letter-spacing: 1px;
    color: var(--navy); text-transform: uppercase; white-space: nowrap;
  }
  .company-note {
    margin-top: 8px;
    font-size: 15px; letter-spacing: 0.5px; color: var(--navy);
  }
  .company-address {
    position: absolute; left: 578px; top: 52px;
    font-size: 19px; line-height: 1.2; color: var(--navy);
  }
  .contact-band {
    position: absolute; left: 0; top: 272px;
    width: 100%; height: 140px;
    background: var(--navy);
  }
  .person {
    position: absolute; right: 420px; top: 38px;
    text-align: right; color: var(--band-text);
  }
  .person-name {
    font-size: 37px; letter-spacing: 2px; text-transform: uppercase; white-space: nowrap;
  }
  .person-title {
    font-size: 17px; letter-spacing: 1.5px; text-transform: uppercase;
    margin-top: 6px;
  }
  .band-divider {
    position: absolute; left: 444px; top: 24px;
    width: 1px; height: 92px; background: var(--divider);
  }
  .contact-list {
    position: absolute; left: 470px; top: 26px;
    list-style: none; color: var(--band-text); font-size: 19px;
  }
  .contact-list li {
    display: flex; align-items: center; gap: 10px; height: 29px;
  }
  .contact-icon { width: 20px; height: 20px; flex: none; }
  .grey-strip {
    position: absolute; left: 0; top: 412px;
    width: 100%; height: 14px; background: var(--strip-grey);
  }
  .card-base {
    position: absolute; left: 0; top: 426px;
    width: 100%; height: 54px; background: var(--base-grey);
  }
</style>
</head>
<body>
  <div class="business-card">
    <div class="brand">
      <span class="brand-mark"></span>
      <div class="brand-text">
        <span class="company-name">Ridgeway Framers</span>
        <span class="company-note">*Registered and Insured</span>
      </div>
    </div>
    <div class="company-address">4417 Cedar Hollow Rd<br>Tampa, FL 33610</div>

    <div class="contact-band">
      <div class="person">
        <div class="person-name">Dana Whitlock</div>
        <div class="person-title">General Manager</div>
      </div>
      <div class="band-divider"></div>
      <ul class="contact-list">
        <li>
          <svg class="contact-icon" viewBox="0 0 20 20" aria-hidden="true">
            <circle cx="10" cy="10" r="9" fill="none" stroke="#e9edf3" stroke-width="1.2"/>
            <rect x="7" y="4.5" width="6" height="11" rx="1" fill="none" stroke="#e9edf3" stroke-width="1.2"/>
          </svg>
          <span>555-201-4410</span>
        </li>
        <li>
          <svg class="contact-icon" viewBox="0 0 20 20" aria-hidden="true">
            <circle cx="10" cy="10" r="9" fill="none" stroke="#e9edf3" stroke-width="1.2"/>
            <path d="M6.5 5.5 L8.5 5 L9.5 7.5 L8.3 8.5 Q9.3 10.8 11.5 11.7 L12.5 10.5 L15 11.5 L14.5 13.5 Q9 14 6.5 5.5 Z" fill="#e9edf3"/>
          </svg>
          <span>555-201-4411</span>
        </li>
        <li>
          <svg class="contact-icon" viewBox="0 0 20 20" aria-hidden="true">
            <circle cx="10" cy="10" r="9" fill="none" stroke="#e9edf3" stroke-width="1.2"/>
            <rect x="5" y="6.5" width="10" height="7" fill="none" stroke="#e9edf3" stroke-width="1.2"/>
            <path d="M5 6.5 L10 10.5 L15 6.5" fill="none" stroke="#e9edf3" stroke-width="1.2"/>
          </svg>
          <span>info@ridgeway.co</span>
        </li>
      </ul>
    </div>
    <div class="grey-strip"></div>
    <div class="card-base"></div>
  </div>
</body>
</html>
```